Elegant Business Cards & Letterhead

We will need the following that need to be designed: Letterhead and Business Cards, there winer will be re-hired for the balance of our stationary needs. Text for the cards and letterheads:

- Corporate Card instead of name
- landline: +971 (4) 362 7041
- mobile: +971 56 2819 605
- 800TUTOR
- email: dubai@velmora-lune.com
- www.velmora-lune.com
- PO Box 387261
Address: Castellan Heights Suite 1708, Dubai UAE

Thank you

Target Market(s)

VIPs, HNWI, High-end Families.

Industry/Entity Type

Luxury Market

Font styles to use
Other font styles liked:
• as explained

Colors

Designer to choose only greyscale colors for use in the design.

Requirements
Must have
• Elegant, Simple, Luxurious, Minimalistic
Nice to have
• Luxury, Golds, Engravings,
Should not have
• Much colors, funky,

```html
<!DOCTYPE html>
<html lang="en">
<head>
<meta charset="utf-8">
<title>Velmora Lune — Stationery</title>
<link rel="stylesheet" href="https://fonts.googleapis.com/css2?family=Marcellus&family=Arimo:wght@400;700&display=swap">
<style>
  :root {
    --backdrop: #6b6c6e;
    --card: #2e2e2e;
    --band: #2f2f2f;
    --silver: #b7b7b7;
    --card-text: #e9e9e9;
    --paper: #ffffff;
    --ink: #1a1a1a;
    --ink-soft: #555555;
    --rule: #222222;
  }
  * { margin: 0; padding: 0; box-sizing: border-box; }
  html, body { width: 1200px; height: 1091px; overflow: hidden; }
  body {
    position: relative;
    background: var(--backdrop);
    font-family: "Arimo", Arial, sans-serif;
  }
  .icon-defs { position: absolute; width: 0; height: 0; }
  .icon { width: 7px; height: 7px; fill: currentColor; flex: none; }

  .wordmark {
    font-family: "Marcellus", serif;
    color: var(--silver);
    white-space: nowrap;
    letter-spacing: 0.02em;
  }

  /* Business card, contact side */
  .card {
    position: absolute;
    background: var(--card);
    border-radius: 12px;
    box-shadow: 2px 2px 3px rgba(0,0,0,0.25);
  }
  .card--contact { left: 124px; top: 317px; width: 359px; height: 205px; }
  .card--contact .wordmark {
    position: absolute; left: 41px; top: 93px;
    font-size: 17px;
  }
  .card-divider {
    position: absolute; left: 188px; top: 43px;
    width: 1px; height: 121px;
    background: linear-gradient(to bottom, transparent, #9a9a9a 20%, #9a9a9a 80%, transparent);
  }
  .card-address {
    position: absolute; left: 205px; top: 57px;
    color: var(--card-text); font-size: 8.6px; line-height: 10.6px;
  }
  .card-contacts {
    position: absolute; left: 205px; top: 94px;
    list-style: none; color: var(--card-text);
    font-size: 8.6px; line-height: 10.6px;
  }
  .card-contacts li { display: flex; align-items: center; gap: 7px; }

  /* Business card, logo side */
  .card--logo { left: 122px; top: 551px; width: 360px; height: 205px; }
  .card--logo .wordmark {
    position: absolute; left: 0; right: 0; top: 87px;
    text-align: center; font-size: 27px;
  }

  /* Letterhead */
  .letterhead {
    position: absolute; left: 513px; top: 146px;
    width: 580px; height: 816px;
    background: var(--paper);
    box-shadow: 2px 2px 3px rgba(0,0,0,0.25);
  }
  .letterhead-band {
    position: absolute; left: 157px; top: 0;
    width: 265px; height: 77px;
    background: var(--band);
    display: flex; align-items: center; justify-content: center;
  }
  .letterhead-band .wordmark { font-size: 27px; padding-top: 6px; }

  .recipient {
    position: absolute; left: 60px; top: 193px;
    font-size: 9.6px; line-height: 11.7px; color: var(--ink);
  }
  .salutation {
    position: absolute; left: 58px; top: 329px;
    font-size: 10.5px; font-weight: 700; color: var(--ink-soft);
  }
  .letter-body {
    position: absolute; left: 58px; top: 368px; width: 472px;
    font-size: 9.5px; line-height: 10.4px; color: var(--ink-soft);
  }
  .letter-body p + p { margin-top: 10.4px; }

  .signature {
    position: absolute; left: 61px; top: 608px;
    color: var(--ink-soft);
  }
  .signature-name { font-size: 11.5px; font-weight: 700; letter-spacing: 0.02em; }
  .signature-role { font-size: 11px; margin-top: 1px; }

  .letter-footer {
    position: absolute; left: 63px; top: 752px; width: 452px;
    color: var(--ink); font-size: 8px; text-align: center;
  }
  .footer-address { padding-bottom: 2px; border-bottom: 1px solid var(--rule); }
  .footer-contacts {
    list-style: none; display: flex; justify-content: center;
    gap: 5px; margin-top: 5px; padding-left: 10px;
  }
  .footer-contacts li { display: flex; align-items: center; gap: 6px; }
</style>
</head>
<body>

<svg class="icon-defs" aria-hidden="true">
  <symbol id="i-phone" viewBox="0 0 24 24"><path d="M6.6 10.8c1.4 2.8 3.8 5.1 6.6 6.6l2.2-2.2c.3-.3.7-.4 1-.2 1.1.4 2.3.6 3.6.6.6 0 1 .4 1 1V20c0 .6-.4 1-1 1C10.6 21 3 13.4 3 4c0-.6.4-1 1-1h3.5c.6 0 1 .4 1 1 0 1.3.2 2.5.6 3.6.1.3 0 .7-.2 1z"/></symbol>
  <symbol id="i-mobile" viewBox="0 0 24 24"><path d="M7 1h10a2 2 0 0 1 2 2v18a2 2 0 0 1-2 2H7a2 2 0 0 1-2-2V3a2 2 0 0 1 2-2zm0 3v15h10V4z"/></symbol>
  <symbol id="i-mail" viewBox="0 0 24 24"><path d="M2 5h20v14H2zm2 2v.5l8 5 8-5V7z"/></symbol>
  <symbol id="i-globe" viewBox="0 0 24 24"><path d="M12 2a10 10 0 1 0 0 20 10 10 0 0 0 0-20zm-1 17.9A8 8 0 0 1 4.2 10L9 15v1a2 2 0 0 0 2 2zm6.9-2.5A2 2 0 0 0 16 16h-1v-3a1 1 0 0 0-1-1H8v-2h2a1 1 0 0 0 1-1V7h2a2 2 0 0 0 2-2v-.4a8 8 0 0 1 2.9 12.8z"/></symbol>
</svg>

<section class="card card--contact" aria-label="Business card, contact side">
  <div class="wordmark">VELMORA LUNE</div>
  <div class="card-divider"></div>
  <address class="card-address" style="font-style:normal">
    PO Box 387261<br>
    Castellan Heights<br>
    Suite 1708, Dubai UAE
  </address>
  <ul class="card-contacts">
    <li><svg class="icon"><use href="#i-phone"/></svg>+971 (4) 362 7041</li>
    <li><svg class="icon"><use href="#i-mobile"/></svg>+971 56 2819 605</li>
    <li><svg class="icon"><use href="#i-phone"/></svg>800TUTOR</li>
    <li><svg class="icon"><use href="#i-mail"/></svg>dubai@velmora-lune.com</li>
    <li><svg class="icon"><use href="#i-globe"/></svg>www.velmora-lune.com</li>
  </ul>
</section>

<section class="card card--logo" aria-label="Business card, brand side">
  <div class="wordmark">VELMORA LUNE</div>
</section>

<article class="letterhead" aria-label="Letterhead">
  <header class="letterhead-band">
    <div class="wordmark">VELMORA LUNE</div>
  </header>

  <div class="recipient">
    Anrede<br>Name<br>Straße<br>PLZ und ORT
  </div>

  <div class="salutation">Dear Sir</div>

  <div class="letter-body">
    <p>Lorem ipsum dolor sit amet. Non quam iste ut dolor repellendus aut quasi porro nam molestias ullam ut sint ipsa! Qui accusamus assumenda qui quae tempore sit quia velit aut porro tempora. Est iste explicabo aut alias impedit est sequi quis.</p>
    <p>Cum rerum molestiae id galisum odit et autem voluptas aut blanditiis iste ut aspernatur itaque ut tempora laudantium vel voluptatem repudiandae! Ea delectus omnis est voluptas odit ut assumenda quisquam eos facere sunt qui quis vitae. Qui velit dolorem in distinctio</p>
    <p>dignissimos rem voluptatem totam ut quia nostrum cum quas consequuntur. Quo aliquid earum eum optio ducimus qui fugiat veniam qui blanditiis velit ut quos dolores non officiis enim ut voluptatem veritatis.</p>
    <p>At quia sunt nam quibusdam mollitia aut rerum laudantium et inventore molestiae aut cumque consequa-tur. 33 minima velit rem quasi galisum ut quae magni sed praesentium possimus 33 commodi quam qui quae aperiam est enim accusantium. Sed Quis laboriosam ut suscipit maxime cum reprehenderit adipisci. Non nihil dolor ut obcaecati commodi aut Quis provident eos doloribus cumque.</p>
    <p>At quia sunt nam quibusdam mollitia aut rerum laudantium et inventore molestiae aut cumque consequa-tur. 33 minima velit rem quasi galisum ut quae</p>
  </div>

  <div class="signature">
    <div class="signature-name">ELIAS VARGA</div>
    <div class="signature-role">Geschäftsführer</div>
  </div>

  <footer class="letter-footer">
    <div class="footer-address">PO Box 387261, Castellan Heights, Suite 1708, Dubai UAE</div>
    <ul class="footer-contacts">
      <li><svg class="icon"><use href="#i-phone"/></svg>+971 (4) 362 7041</li>
      <li><svg class="icon"><use href="#i-phone"/></svg>800TUTOR</li>
      <li><svg class="icon"><use href="#i-mail"/></svg>dubai@velmora-lune.com</li>
      <li><svg class="icon"><use href="#i-globe"/></svg>www.velmora-lune.com</li>
    </ul>
  </footer>
</article>

</body>
</html>
```